Custom Wordpress Theme - Original and Professional

We are a boutique IT consulting firm that provide small and medium business in Australia three different levels of IT service.
We are looking for a developer who will create a customised, original and professional wordpress theme. We are looking for the developer to create a professional, clean, clear and simple theme with a stylish layout, images and icons.
Our three services are: IT support | IT Services | IT Solutions and we would like to clearly differentiate the difference in each level of service in as few words as possible.
IT Support is the ad hock “call us, when you need us” service, that smaller business or those with minimal issues use.
IT service is the unlimited service, that business with existing (and well maintained) IT systems choose and is both flexible and scalable including no contracts or paperwork required.
IT solutions are the unlimited service that businesses that need new or updated infrastructure choose and it includes all the hardware, software and services with no contracts or any ongoing commitment.
The main page on the web site will attract the visitor to choose the right “service level” for their business and then we will have a dedicated page for each service and another page for a comparison (table) to compare all three services.
Lastly we will need a contact us page that has both office locations (Sydney and Melbourne), contact phone numbers and an email form.
Items we are focused on for this project are: 1. Images, 2.Icons 3. Layout.
In summary we are looking for a custom WordPress theme into a 6 page (Home, IT Support, IT Services, IT Solutions, Compare Service levels and Contact us) website. The design must include relevant images and icons and be clear, simple, professional and sleek.

Thank you for your time and creativity and I look forward to working with you!

Target Market(s)

Small and Medium businesses in Australia

Industry/Entity Type

Boutique

Requirements
Must have
• - 6 Pages layout: Home, IT support, IT services, IT Solutions, Compare service levels and Contact us
- Images, Layout and Icons.
- Clean, Clear, Simple, Elegant, Stylish.
Nice to have
• - Some text (if possible but not required).
Should not have
• - Complexity.
- Confusing layout.
- Generic non matching images and icons.

```html
<!DOCTYPE html>
<html lang="en">
<head>
<meta charset="utf-8">
<title>IT Solution</title>
<link rel="stylesheet" href="https://fonts.googleapis.com/css2?family=Marcellus&family=Noto+Sans:ital,wght@0,400;0,700;1,400&display=swap">
<style>
  :root {
    --ink: #111111;
    --muted: #8a8a8a;
    --title: #5a5a5a;
    --accent: #3cdde3;
    --bullet: #e2473f;
    --rule: #9aa3ad;
    --hero-top: #d9dcdf;
    --hero-mid: #eceeef;
    --hero-key: #8feaf0;
    --white: #ffffff;
  }
  * { box-sizing: border-box; margin: 0; padding: 0; }
  html, body { width: 840px; height: 1200px; overflow: hidden; background: var(--white); }
  body { position: relative; font-family: "Noto Sans", sans-serif; color: var(--ink); }

  .brand { position: absolute; left: 44px; top: 56px; }
  .brand-name { font-family: "Marcellus", serif; font-size: 21px; letter-spacing: 0.3px; color: var(--ink); line-height: 1; }
  .brand-slogan { margin: 7px 0 0 20px; font-size: 7.5px; color: var(--muted); text-transform: uppercase; letter-spacing: 0.2px; }

  .main-nav { position: absolute; top: 63px; left: 0; width: 840px; font-size: 12px; }
  .main-nav a { position: absolute; white-space: nowrap; color: var(--ink); text-decoration: none; }
  .main-nav a.is-current { color: var(--accent); }

  .header-rule { position: absolute; left: 36px; top: 118px; width: 770px; height: 1px; background: var(--rule); }

  .hero { position: absolute; left: 18px; top: 121px; width: 788px; height: 270px;
    background: radial-gradient(ellipse 40% 28% at 56% 54%, var(--hero-key) 0%, var(--hero-key) 55%, rgba(143,234,240,0) 100%),
                linear-gradient(180deg, var(--hero-top) 0%, var(--hero-mid) 50%, var(--hero-top) 100%); }

  .page-head { position: absolute; left: 50px; top: 410px; }
  .page-title { font-family: "Marcellus", serif; font-size: 12px; font-weight: 400; color: var(--title); }
  .breadcrumb { margin-top: 5px; font-size: 6.5px; font-style: italic; color: var(--ink); }
  .breadcrumb .current { color: var(--accent); }

  .content { position: absolute; left: 44px; top: 522px; width: 534px; font-size: 11.7px; line-height: 20.2px; text-align: justify; }
  .content p + p { margin-top: 20px; }

  .side-list { position: absolute; left: 606px; list-style: none; font-size: 7.4px; color: var(--accent); }
  .side-list li { position: relative; padding-left: 11px; height: 22px; line-height: 10px; }
  .side-list li:nth-child(n+5) { height: 24px; }
  .side-list svg { position: absolute; left: 0; top: 2px; }
  .side-list.first { top: 520px; }
  .side-list.second { top: 689px; }

  .footer { position: absolute; left: 0; top: 1153px; width: 840px; height: 47px; background: var(--accent); color: var(--white); }
  .footer-note { position: absolute; left: 54px; top: 15px; font-size: 12px; }
  .social { position: absolute; right: 40px; top: 20px; display: flex; gap: 4px; }
  .social span { width: 7px; height: 7px; border-radius: 50%; background: var(--white); }
</style>
</head>
<body>
  <header>
    <div class="brand">
      <div class="brand-name">COMPANY NAME</div>
      <div class="brand-slogan">Your company solgan</div>
    </div>
    <nav class="main-nav">
      <a style="left:351px" href="#">Home</a>
      <a style="left:402px" href="#">IT support</a>
      <a style="left:475px" href="#">IT Services</a>
      <a style="left:548px" class="is-current" href="#">IT Solutions</a>
      <a style="left:628px" href="#">Compare Service</a>
      <a style="left:733px" href="#">Contact us</a>
    </nav>
    <div class="header-rule"></div>
  </header>

  <div class="hero" role="img" aria-label="Close-up of a white keyboard with a turquoise key labelled Solution"></div>

  <div class="page-head">
    <h1 class="page-title">IT Solution</h1>
    <div class="breadcrumb">HOME | <span class="current">IT Solution</span></div>
  </div>

  <main class="content">
    <p>Lorem ipsum dolor sit amet, consectetur adipiscing elit. Praesent nec euismod diam, ac gravida elit. In ac sagittis velit. Integer aliquet arcu ut dapibus bibendum. Donec non sodales purus. Maecenas in ipsum id ligula tempus egestas non at diam. Pellentesque sed lectus nisi. Sed commodo nunc lorem, quis pharetra tortor feugiat quis. Nullam in nisi suscipit nisi luctus semper. Proin hendrerit mauris non tempor facilisis. Pellentesque nec metus interdum, gravida erat sed, malesuada felis. Cras tincidunt nisi et auctor pellentesque. Donec sed augue in elit gravida mollis. Nam imperdiet lectus nec sapien consequat fringilla non sed lacus. Nam porta accumsan eros, id scelerisque nunc varius eget.</p>
    <p>Aliquam erat volutpat. Donec a leo dictum, dictum elit et, ornare lacus. Mauris tempor lacus est, quis cursus ipsum venenatis eget. Proin sollicitudin tristique sem ac faucibus. Pellentesque ut dignissim dui. Pellentesque gravida at velit id aliquet. Sed adipiscing varius mollis. In convallis hendrerit leo id gravida. Suspendisse facilisis blandit nisl eget blandit. Sed sit amet dignissim risus, ac luctus eros. Curabitur egestas vestibulum lacus. Etiam id vulputate turpis. Phasellus diam magna, pulvinar eget felis convallis, tincidunt rutrum purus. Morbi erat risus, cursus eleifend leo et, sagittis vestibulum risus. Ut vel dolor ac enim porttitor aliquet.</p>
  </main>

  <ul class="side-list first">
    <li><svg width="7" height="8" viewBox="0 0 7 8"><path d="M1 0 L6 4 L1 8 L0 6.5 L3.5 4 L0 1.5 Z" fill="var(--bullet)"/></svg>Aenean nonummy hendrerit ma</li>
    <li><svg width="7" height="8" viewBox="0 0 7 8"><path d="M1 0 L6 4 L1 8 L0 6.5 L3.5 4 L0 1.5 Z" fill="var(--bullet)"/></svg>Fusce suscipit varius mi</li>
    <li><svg width="7" height="8" viewBox="0 0 7 8"><path d="M1 0 L6 4 L1 8 L0 6.5 L3.5 4 L0 1.5 Z" fill="var(--bullet)"/></svg>Cum sociis natoque penatibus</li>
    <li><svg width="7" height="8" viewBox="0 0 7 8"><path d="M1 0 L6 4 L1 8 L0 6.5 L3.5 4 L0 1.5 Z" fill="var(--bullet)"/></svg>Fusce feugiat malesuada odio</li>
    <li><svg width="7" height="8" viewBox="0 0 7 8"><path d="M1 0 L6 4 L1 8 L0 6.5 L3.5 4 L0 1.5 Z" fill="var(--bullet)"/></svg>Morbi nunc odio, gravida</li>
    <li><svg width="7" height="8" viewBox="0 0 7 8"><path d="M1 0 L6 4 L1 8 L0 6.5 L3.5 4 L0 1.5 Z" fill="var(--bullet)"/></svg>Morbi nunc odio, gravida</li>
  </ul>

  <ul class="side-list second">
    <li><svg width="7" height="8" viewBox="0 0 7 8"><path d="M1 0 L6 4 L1 8 L0 6.5 L3.5 4 L0 1.5 Z" fill="var(--bullet)"/></svg>Aenean nonummy hendrerit ma</li>
    <li><svg width="7" height="8" viewBox="0 0 7 8"><path d="M1 0 L6 4 L1 8 L0 6.5 L3.5 4 L0 1.5 Z" fill="var(--bullet)"/></svg>Fusce suscipit varius mi</li>
    <li><svg width="7" height="8" viewBox="0 0 7 8"><path d="M1 0 L6 4 L1 8 L0 6.5 L3.5 4 L0 1.5 Z" fill="var(--bullet)"/></svg>Cum sociis natoque penatibus</li>
    <li><svg width="7" height="8" viewBox="0 0 7 8"><path d="M1 0 L6 4 L1 8 L0 6.5 L3.5 4 L0 1.5 Z" fill="var(--bullet)"/></svg>Fusce feugiat malesuada odio</li>
    <li><svg width="7" height="8" viewBox="0 0 7 8"><path d="M1 0 L6 4 L1 8 L0 6.5 L3.5 4 L0 1.5 Z" fill="var(--bullet)"/></svg>Morbi nunc odio, gravida</li>
    <li><svg width="7" height="8" viewBox="0 0 7 8"><path d="M1 0 L6 4 L1 8 L0 6.5 L3.5 4 L0 1.5 Z" fill="var(--bullet)"/></svg>Morbi nunc odio, gravida</li>
  </ul>

  <footer class="footer">
    <div class="footer-note">IT SOLUTION© 2013 • Privacy Policy</div>
    <div class="social" aria-label="Social links">
      <span></span><span></span><span></span><span></span>
    </div>
  </footer>
</body>
</html>
```